Commercial and Residential Paint Contractor needs website

We need a website for our residential painting, multi-family painting and commercial painting company. We paint interior and exterior of houses, apartments and commercial buildings. I would like an about us page, residential page, multi family page, commercial page and contact us. Need keywords added to website for seo opitimazation. I like this website https://www.glossfieldworks.com/

Target Market(s)

General Contractors and commercial property managers

Coding

Coded - Design and coding required

Number of Pages Required

5+ page

Font styles to use
Sans Serif

Requirements
Must have
• I need SEO keywords on pages

```html
<!DOCTYPE html>
<html lang="en">
<head>
<meta charset="utf-8">
<meta name="format-detection" content="telephone=no">
<title>Hollis Painting — Residential, Multi-Family &amp; Commercial Painting</title>
<meta name="description" content="Hollis Painting: residential painting, multi-family painting and commercial painting contractor for interior and exterior projects.">
<link rel="stylesheet" href="https://fonts.googleapis.com/css2?family=Rubik:wght@500;700;800&family=Open+Sans:wght@400;600;700&display=swap">
<style>
:root{
  --navy:#0f3a8c;
  --navy-dark:#0d367f;
  --red:#c1112b;
  --ink:#222;
  --muted:#444;
  --white:#fff;
  --line:#cfd4de;
}
*{box-sizing:border-box;margin:0;padding:0}
html,body{width:1200px;height:3360px;overflow:hidden}
body{position:relative;font-family:"Open Sans",Arial,sans-serif;color:var(--ink);background:#fff}
a{color:inherit;text-decoration:none}
.abs{position:absolute}
.btn{position:absolute;background:var(--red);color:#fff;font-family:"Rubik",Arial,sans-serif;font-weight:700;text-transform:uppercase;display:flex;align-items:center;justify-content:center;letter-spacing:.3px}
.section-title{position:absolute;left:0;width:1200px;text-align:center;font-family:"Rubik",Arial,sans-serif;font-weight:700;font-size:30px;color:var(--navy);letter-spacing:-.3px}
.rule{position:absolute;left:579px;width:42px;height:3px;background:var(--red)}

/* header */
.site-header{top:0;left:0;width:1200px;height:114px;background:#fff}
.brand{left:130px;top:22px;font-family:"Rubik",Arial,sans-serif;font-weight:800;color:var(--navy);font-size:40px;line-height:1;letter-spacing:1px}
.brand small{display:block;font-size:19px;letter-spacing:7px;margin-top:4px;color:var(--navy)}
.contact-chip{display:flex;align-items:center;gap:10px;top:22px}
.chip-icon{width:30px;height:30px;border-radius:50%;background:var(--red);display:flex;align-items:center;justify-content:center}
.chip-label{font-size:12px;color:var(--navy);line-height:1.1}
.chip-value{font-size:17px;font-weight:700;color:var(--navy);line-height:1.2}
.main-nav{top:79px;right:135px;display:flex;gap:30px;font-family:"Rubik",Arial,sans-serif;font-weight:500;font-size:14px;color:var(--navy)}
.main-nav .active{color:var(--red);text-decoration:underline;text-underline-offset:4px}

/* hero */
.hero{top:114px;left:0;width:1200px;height:541px;background:linear-gradient(180deg,#8fb3de 0%,#c9dbef 35%,#d9b870 60%,#8a8f6a 100%)}
.hero-title{left:130px;top:66px;font-family:"Rubik",Arial,sans-serif;font-weight:700;font-size:47px;line-height:50px;color:var(--navy);letter-spacing:.5px}
.dots{display:flex;gap:12px;align-items:center}
.dot{width:7px;height:7px;border-radius:50%;background:#fff}
.dot.on{width:12px;height:12px;background:var(--red);border:2px solid #fff}

/* services */
.service{width:296px}
.service .photo{position:absolute;left:0;top:0;width:296px;height:309px}
.service .panel{position:absolute;left:0;top:276px;width:285px;height:140px;background:#fff}
.service h3{position:absolute;left:30px;top:14px;font-family:"Rubik",Arial,sans-serif;font-weight:700;font-size:15px;color:var(--navy)}
.service p{position:absolute;left:30px;top:41px;width:240px;font-size:11.5px;line-height:16px;color:var(--ink)}
.service .btn{left:34px;top:98px;width:84px;height:26px;font-size:10px}

/* welcome */
.welcome{top:1226px;left:0;width:1200px;height:446px;background:linear-gradient(90deg,#eef3f7 0%,#dbeaf2 30%,#b5daec 55%,#c6e3f1 100%)}
.welcome-photo{left:0;top:0;width:480px;height:446px;background:linear-gradient(90deg,#e9eef3 0%,#c9d9ea 50%,rgba(180,216,236,0) 100%)}
.welcome-sub{left:661px;top:48px;font-family:"Rubik",Arial,sans-serif;font-weight:500;font-size:19px;color:var(--navy)}
.welcome-title{left:658px;top:70px;font-family:"Rubik",Arial,sans-serif;font-weight:700;font-size:37px;color:var(--navy)}
.welcome-title::after{content:"";position:absolute;left:0;top:50px;width:123px;height:3px;background:var(--red)}
.welcome-copy{left:658px;top:158px;width:414px;font-size:14.8px;line-height:20px;color:#333}

/* testimonials */
.testimonials{top:1672px;left:0;width:1200px;height:459px;background:var(--navy-dark)}
.quote-box{width:445px;height:210px;border:1px solid rgba(255,255,255,.8)}
.quote-box .mark{position:absolute;font-family:Georgia,serif;font-weight:700;font-size:46px;color:#fff;background:var(--navy-dark);line-height:1;padding:0 3px}
.stars{position:absolute;left:44px;top:24px;color:#fff;font-size:12px;letter-spacing:1px}
.quote-box p{position:absolute;left:44px;top:46px;width:372px;font-size:12.3px;line-height:17.7px;color:#fff}
.quote-box .rule-sm{position:absolute;left:48px;top:152px;width:44px;height:2px;background:#fff;border-radius:2px}
.quote-box .name{position:absolute;left:47px;top:163px;font-size:11px;font-weight:700;color:#fff}

/* blog */
.blog-card{width:461px;height:242px;border:1px solid #bdbdbd;background:#fff}
.blog-card .photo{position:absolute;left:-1px;top:-1px;width:231px;height:242px}
.blog-card .date{position:absolute;left:258px;top:28px;font-size:11.5px;color:#333}
.blog-card h4{position:absolute;left:258px;top:48px;width:180px;font-family:"Rubik",Arial,sans-serif;font-weight:700;font-size:12.3px;line-height:17.5px;color:#111;text-transform:uppercase}
.blog-card p{position:absolute;left:258px;top:111px;width:180px;font-size:11.3px;line-height:14.5px;color:#333}
.blog-card .btn{left:261px;top:187px;width:80px;height:22px;font-size:10px}
.arrow-btn{width:35px;height:35px;background:#222;display:flex;align-items:center;justify-content:center}

/* contact */
.contact{top:2552px;left:0;width:1200px;height:468px;background:linear-gradient(180deg,#eef0f4 0%,#f4f3f1 60%,#f1efec 100%)}
.field{position:absolute;height:42px;width:246px;background:#fff;border:1px solid var(--line);font-size:12px;color:#333;padding:0 15px;display:flex;align-items:center;justify-content:space-between}
.field.msg{align-items:flex-start;padding-top:14px}

/* footer */
.site-footer{top:3020px;left:0;width:1200px;height:340px;background:var(--navy-dark);color:#fff}
.foot-brand{left:143px;top:95px;font-family:"Rubik",Arial,sans-serif;font-weight:800;font-size:52px;line-height:1;color:#fff;letter-spacing:2px}
.foot-brand small{display:block;font-size:21px;letter-spacing:9px;margin-top:4px}
.foot-head{font-family:"Rubik",Arial,sans-serif;font-weight:700;font-size:13px;letter-spacing:.5px}
.foot-menu{left:480px;top:94px;font-size:12px;line-height:20px;text-transform:uppercase}
.foot-item{display:flex;gap:12px;align-items:flex-start;font-size:12px;line-height:16px}
.foot-icon{width:24px;height:24px;border-radius:50%;background:#fff;flex:none;display:flex;align-items:center;justify-content:center}
.foot-divider{left:130px;top:266px;width:940px;height:1px;background:rgba(255,255,255,.25)}
.copyright{left:0;top:308px;width:1200px;text-align:center;font-size:9.5px}
</style>
</head>
<body>

<header class="abs site-header">
  <div class="abs brand">HOLLIS<small>PAINTING</small></div>
  <div class="abs contact-chip" style="left:656px">
    <div class="chip-icon"><svg width="14" height="14" viewBox="0 0 14 14"><rect x="1" y="3" width="12" height="8" fill="#fff"/><path d="M1 3l6 5 6-5" stroke="#c1112b" stroke-width="1.4" fill="none"/></svg></div>
    <div><div class="chip-label">E MAIL US</div><div class="chip-value">info@hollispainting.com</div></div>
  </div>
  <div class="abs contact-chip" style="left:916px">
    <div class="chip-icon"><svg width="14" height="14" viewBox="0 0 24 24"><path fill="#fff" d="M6.6 10.8a15.1 15.1 0 006.6 6.6l2.2-2.2c.3-.3.7-.4 1-.2 1.1.4 2.3.6 3.6.6.6 0 1 .4 1 1V20c0 .6-.4 1-1 1A17 17 0 013 4c0-.6.4-1 1-1h3.5c.6 0 1 .4 1 1 0 1.2.2 2.5.6 3.6.1.3 0 .7-.2 1z"/></svg></div>
    <div><div class="chip-label">CALL US</div><div class="chip-value">555.214.0387</div></div>
  </div>
  <nav class="abs main-nav">
    <span class="active">HOME</span><span>ABOUT</span><span>RESIDENTIAL</span><span>MULTI FAMILY</span><span>COMMERCIAL</span><span>CONTACT US</span>
  </nav>
</header>

<section class="abs hero" role="img" aria-label="Photo of a freshly painted yellow craftsman house with white trim under a blue sky">
  <h1 class="abs hero-title">RESIDENTIAL<br>PAINTING</h1>
  <div class="btn" style="left:134px;top:186px;width:135px;height:43px;font-size:16px">READ MORE</div>
  <div class="abs dots" style="left:556px;top:492px"><span class="dot"></span><span class="dot"></span><span class="dot on"></span><span class="dot"></span><span class="dot"></span></div>
</section>

<section class="abs" style="top:655px;left:0;width:1200px;height:571px">
  <h2 class="section-title" style="top:38px">OUR SERVICES</h2>
  <div class="rule" style="top:80px"></div>

  <article class="abs service" style="left:130px;top:125px">
    <div class="photo" role="img" aria-label="Photo of a two-storey house exterior being painted" style="background:linear-gradient(180deg,#9fc1e3,#b89778 60%,#8c7a68)"></div>
    <div class="panel"><h3>RESIDENTIAL PAINTING</h3><p>Lorem Ipsum is simply dummy text of the printing and typesetting industry.</p><div class="btn">READ MORE</div></div>
  </article>
  <article class="abs service" style="left:452px;top:125px">
    <div class="photo" role="img" aria-label="Photo of a family relaxing in a bright apartment living room" style="background:linear-gradient(180deg,#e6e6e2,#cfc6b9 55%,#b9a48e)"></div>
    <div class="panel"><h3>MULTI-FAMILY PAINTING</h3><p>Lorem Ipsum is simply dummy text of the printing and typesetting industry.</p><div class="btn">READ MORE</div></div>
  </article>
  <article class="abs service" style="left:771px;top:125px">
    <div class="photo" role="img" aria-label="Photo of a roped painter rolling yellow paint onto a commercial wall" style="background:linear-gradient(90deg,#c9cdd0 0%,#9aa3a6 45%,#e0b73a 75%,#d6a928)"></div>
    <div class="panel"><h3>COMMERCIAL PAINTING</h3><p>Lorem Ipsum is simply dummy text of the printing and typesetting industry.</p><div class="btn">READ MORE</div></div>
  </article>
</section>

<section class="abs welcome">
  <div class="abs welcome-photo" role="img" aria-label="Photo of a painter in a blue shirt rolling white paint on a light blue wall"></div>
  <div class="abs welcome-sub">WELCOME TO</div>
  <h2 class="abs welcome-title">HOLLIS PAINTING</h2>
  <p class="abs welcome-copy">Sed ut perspiciatis unde omnis iste natus error sit voluptatem accusantium doloremque laudantium, totam rem aperiam, eaque ipsa quae ab illo inventore veritatis et quasi architecto beatae vitae dicta sunt explicabo. Nemo enim ipsam voluptatem quia voluptas sit aspernatur aut odit aut fugit, sed quia consequuntur magni dolores eos qui ratione voluptatem sequi nesciunt. Neque porro quisquam est, qui dolorem ipsum quia dolo.</p>
  <div class="btn" style="left:661px;top:350px;width:126px;height:40px;font-size:15px">READ MORE</div>
</section>

<section class="abs testimonials">
  <h2 class="section-title" style="top:60px;color:#fff">TESTIMONIALS</h2>
  <div class="rule" style="top:93px;background:#fff"></div>

  <div class="abs quote-box" style="left:133px;top:141px">
    <span class="mark" style="left:-10px;top:-10px">“</span>
    <div class="stars">★★★★★</div>
    <p>Sed ut perspiciatis unde omnis iste natus error sit voluptatem accusantium doloremque laudantium, totam rem aperiam, eaque ipsa quae ab illo inventore veritatis et quasi architecto beatae vitae dicta sunt explicabo. Nemo enim ipsam voluptatem quia voluptas sit aspernatur.</p>
    <div class="rule-sm"></div><div class="name">DANIEL</div>
    <span class="mark" style="right:-10px;bottom:-30px">”</span>
  </div>
  <div class="abs quote-box" style="left:621px;top:141px">
    <span class="mark" style="left:-10px;top:-10px">“</span>
    <div class="stars">★★★★★</div>
    <p>Sed ut perspiciatis unde omnis iste natus error sit voluptatem accusantium doloremque laudantium, totam rem aperiam, eaque ipsa quae ab illo inventore veritatis et quasi architecto beatae vitae dicta sunt explicabo. Nemo enim ipsam voluptatem quia voluptas sit aspernatur.</p>
    <div class="rule-sm"></div><div class="name">DANIEL</div>
    <span class="mark" style="right:-10px;bottom:-30px">”</span>
  </div>

  <div class="abs dots" style="left:537px;top:402px;gap:10px">
    <svg width="10" height="12" viewBox="0 0 10 12"><path d="M7 1L2 6l5 5" stroke="#fff" stroke-width="1.8" fill="none"/></svg>
    <span class="dot" style="width:6px;height:6px"></span><span class="dot" style="width:6px;height:6px"></span><span class="dot on"></span><span class="dot" style="width:6px;height:6px"></span><span class="dot" style="width:6px;height:6px"></span>
    <svg width="10" height="12" viewBox="0 0 10 12"><path d="M3 1l5 5-5 5" stroke="#fff" stroke-width="1.8" fill="none"/></svg>
  </div>
</section>

<section class="abs" style="top:2131px;left:0;width:1200px;height:421px">
  <h2 class="section-title" style="top:44px">LATEST BLOG</h2>
  <div class="rule" style="top:92px"></div>

  <div class="abs arrow-btn" style="left:114px;top:240px"><svg width="10" height="14" viewBox="0 0 10 14"><path d="M7 1L2 7l5 6" stroke="#fff" stroke-width="1.8" fill="none"/></svg></div>
  <div class="abs arrow-btn" style="left:1052px;top:240px"><svg width="10" height="14" viewBox="0 0 10 14"><path d="M3 1l5 6-5 6" stroke="#fff" stroke-width="1.8" fill="none"/></svg></div>

  <article class="abs blog-card" style="left:130px;top:135px">
    <div class="photo" role="img" aria-label="Photo of a painter on a ladder painting a house window frame" style="background:linear-gradient(180deg,#9ab7db,#d6c7ad 55%,#b8a68e)"></div>
    <div class="date">08/08/2020</div>
    <h4>Sed ut perspiciatis unde omnis iste natus error sit voluptatem</h4>
    <p>Sed ut perspiciatis unde omnis iste natus error sit voluptatem accusantium doloremque lau dantium, totam rem.</p>
    <div class="btn">READ MORE</div>
  </article>
  <article class="abs blog-card" style="left:605px;top:135px">
    <div class="photo" role="img" aria-label="Photo of a paint roller spreading bright red paint on a wall" style="background:linear-gradient(90deg,#e8202a,#f0474b 60%,#f4d7d5)"></div>
    <div class="date">08/08/2020</div>
    <h4>Sed ut perspiciatis unde omnis iste natus error sit voluptatem</h4>
    <p>Sed ut perspiciatis unde omnis iste natus error sit voluptatem accusantium doloremque lau dantium, totam rem.</p>
    <div class="btn">READ MORE</div>
  </article>
</section>

<section class="abs contact">
  <h2 class="section-title" style="top:44px">CONTACT US</h2>
  <div class="rule" style="top:92px"></div>
  <div class="field" style="left:219px;top:130px">FIRST NAME</div>
  <div class="field" style="left:477px;top:130px">LAST NAME</div>
  <div class="field" style="left:734px;top:130px">PHONE</div>
  <div class="field" style="left:219px;top:185px">E MAIL</div>
  <div class="field" style="left:477px;top:185px">SELECT SERVICE <svg width="8" height="5" viewBox="0 0 8 5"><path d="M0 0h8L4 5z" fill="#333"/></svg></div>
  <div class="field" style="left:734px;top:185px">SUBJECT</div>
  <div class="field msg" style="left:219px;top:241px;width:761px;height:116px">MESSAGE</div>
  <div class="btn" style="left:549px;top:389px;width:102px;height:40px;font-size:15px">SUBMIT</div>
</section>

<footer class="abs site-footer">
  <div class="abs foot-brand">HOLLIS<small>PAINTING</small></div>

  <div class="abs foot-head" style="left:480px;top:57px">MENU</div>
  <div class="abs foot-menu">HOME<br>ABOUT<br>RESIDENTIAL<br>MULTI FAMILY<br>COMMERCIAL<br>CONTACT US</div>

  <div class="abs foot-head" style="left:690px;top:57px">CONTACT US</div>
  <div class="abs foot-item" style="left:688px;top:93px">
    <span class="foot-icon"><svg width="10" height="13" viewBox="0 0 10 13"><path d="M5 0a5 5 0 00-5 5c0 3.5 5 8 5 8s5-4.5 5-8a5 5 0 00-5-5z" fill="#0d367f"/><circle cx="5" cy="5" r="1.8" fill="#fff"/></svg></span>
    <span>482 Linden Ave, Ste 12<br>Maple Falls, Texas 75000, US</span>
  </div>
  <div class="abs foot-item" style="left:688px;top:145px">
    <span class="foot-icon"><svg width="11" height="11" viewBox="0 0 24 24"><path fill="#0d367f" d="M6.6 10.8a15.1 15.1 0 006.6 6.6l2.2-2.2c.3-.3.7-.4 1-.2 1.1.4 2.3.6 3.6.6.6 0 1 .4 1 1V20c0 .6-.4 1-1 1A17 17 0 013 4c0-.6.4-1 1-1h3.5c.6 0 1 .4 1 1 0 1.2.2 2.5.6 3.6.1.3 0 .7-.2 1z"/></svg></span>
    <span>Call Us<br>555.214.0387</span>
  </div>
  <div class="abs foot-item" style="left:688px;top:196px">
    <span class="foot-icon"><svg width="11" height="9" viewBox="0 0 12 9"><rect width="12" height="9" fill="#0d367f"/><path d="M0 0l6 5 6-5" stroke="#fff" stroke-width="1.2" fill="none"/></svg></span>
    <span>E mail Us<br>info@hollispainting.com</span>
  </div>

  <div class="abs foot-head" style="left:958px;top:57px">FOLLOW US</div>
  <div class="abs foot-item" style="left:958px;top:93px"><span class="foot-icon"></span><span>Like us on<br>OUR PAGE</span></div>
  <div class="abs foot-item" style="left:958px;top:143px"><span class="foot-icon"></span><span>Follow us on<br>OUR NEWS</span></div>
  <div class="abs foot-item" style="left:958px;top:194px"><span class="foot-icon"></span><span>Follow us on<br>OUR NETWORK</span></div>

  <div class="abs foot-divider"></div>
  <div class="abs copyright">Copyright © 2020 All Rights Reserved</div>
</footer>

</body>
</html>
```